Modern Business Card

Modern professional business card with more than just logo and demographic info. Something memorable.

We are a trendy/modern chiropractic group with an emphasis on neurology, hence the minimalist-type brain logo. We want to convey that modern and technical aspect with professionalism and the elite nature of our practice environment.

```html
<!DOCTYPE html>
<html lang="en">
<head>
<meta charset="utf-8">
<title>Clarity Spine – Business Card</title>
<link rel="stylesheet" href="https://fonts.googleapis.com/css2?family=Montserrat:wght@400;500;700&display=swap">
<style>
  :root {
    --stage: #e9eaec;
    --brand-blue: #4a85c8;
    --brand-blue-light: #5690d2;
    --brand-blue-deep: #3f7bc2;
    --pattern-tint: rgba(255, 255, 255, 0.14);
    --ink: #1d1d1f;
    --ink-soft: #555a60;
    --card-white: #ffffff;
    --rule: #8a8f96;
  }
  * { box-sizing: border-box; margin: 0; padding: 0; }
  html, body {
    width: 1200px; height: 909px; overflow: hidden;
    background: var(--stage);
    font-family: "Montserrat", Arial, sans-serif;
  }
  .stage {
    width: 1200px; height: 909px;
    display: flex; align-items: center; justify-content: center; gap: 40px;
  }
  .card {
    width: 540px; height: 309px;
    border-radius: 3px;
    box-shadow: 0 6px 18px rgba(0,0,0,.18);
    position: relative; overflow: hidden;
  }
  .brand {
    display: flex; align-items: center; gap: 12px;
    position: relative; z-index: 1;
  }
  .brand__dot { width: 18px; height: 18px; border-radius: 50%; flex: none; }
  .brand__name {
    font-weight: 500; letter-spacing: 2px; text-transform: uppercase; white-space: nowrap;
  }

  /* back */
  .card--back {
    background: linear-gradient(200deg, var(--brand-blue-deep) 0%, var(--brand-blue) 50%, var(--brand-blue-light) 100%);
    display: flex; align-items: center; justify-content: center;
  }
  .card__pattern {
    position: absolute;
    left: 90px; top: -30px;
    width: 380px; height: 370px;
    border-radius: 60px;
    background: linear-gradient(125deg,
      rgba(255,255,255,0) 0%,
      var(--pattern-tint) 30%,
      rgba(255,255,255,0.18) 55%,
      var(--pattern-tint) 75%,
      rgba(255,255,255,0) 100%);
    transform: rotate(-8deg);
  }
  .card--back .brand__dot { background: var(--card-white); }
  .card--back .brand__name { color: var(--card-white); font-size: 34px; }

  /* front */
  .card--front { background: var(--card-white); }
  .card--front .brand {
    position: absolute; top: 52px; left: 0; right: 0; justify-content: center;
  }
  .card--front .brand__dot { background: var(--brand-blue); width: 14px; height: 14px; }
  .card--front .brand__name { color: var(--ink); font-size: 26px; }
  .person {
    position: absolute; top: 118px; left: 0; right: 0; text-align: center;
  }
  .person__name {
    color: var(--brand-blue); font-weight: 700; font-size: 19px; letter-spacing: .5px;
  }
  .person__role { color: var(--ink-soft); font-size: 12px; margin-top: 2px; }
  .details {
    position: absolute; top: 196px; left: 0; right: 0;
    display: flex; justify-content: center; align-items: center;
  }
  .address {
    color: var(--ink-soft); font-size: 11.5px; line-height: 1.55;
    text-align: right; padding-right: 18px;
  }
  .divider { width: 1px; height: 62px; background: var(--rule); }
  .contact {
    list-style: none; padding-left: 18px;
    color: var(--ink-soft); font-size: 11.5px; line-height: 1.75;
  }
  .contact li { display: flex; align-items: center; gap: 7px; }
  .contact svg { width: 10px; height: 10px; fill: var(--brand-blue); flex: none; }
</style>
</head>
<body>
<main class="stage">
  <section class="card card--back" aria-label="Card back">
    <div class="card__pattern" role="img" aria-label="Faint translucent rounded diagonal bars with a speckled texture strip"></div>
    <div class="brand">
      <span class="brand__dot"></span>
      <span class="brand__name">Clarity Spine</span>
    </div>
  </section>

  <section class="card card--front" aria-label="Card front">
    <div class="brand">
      <span class="brand__dot"></span>
      <span class="brand__name">Clarity Spine</span>
    </div>
    <div class="person">
      <p class="person__name">DANIEL MORROW</p>
      <p class="person__role">Senior Partner</p>
    </div>
    <div class="details">
      <p class="address">12 Keller Avenue Northcliff,<br>Johannesburg, 2195</p>
      <span class="divider"></span>
      <ul class="contact">
        <li>
          <svg viewBox="0 0 24 24" aria-hidden="true"><path d="M6.6 10.8a15.2 15.2 0 0 0 6.6 6.6l2.2-2.2a1 1 0 0 1 1-.25 11.4 11.4 0 0 0 3.6.57 1 1 0 0 1 1 1V20a1 1 0 0 1-1 1A17 17 0 0 1 3 4a1 1 0 0 1 1-1h3.5a1 1 0 0 1 1 1c0 1.25.2 2.45.57 3.57a1 1 0 0 1-.25 1z"/></svg>
          +120 5550 1784
        </li>
        <li>
          <svg viewBox="0 0 24 24" aria-hidden="true"><path d="M2 5h20v14H2zm2 2v.4l8 5 8-5V7zm0 2.7V17h16V9.7l-8 5z"/></svg>
          info@clarityspine.com
        </li>
        <li>
          <svg viewBox="0 0 24 24" aria-hidden="true"><circle cx="12" cy="12" r="10"/></svg>
          www.clarityspine.com
        </li>
      </ul>
    </div>
  </section>
</main>
</body>
</html>
```